Property development & Investment company Need a logo & business card design

Our name is KT Estates Australia Pty Ltd
Need logo & business card design

Target Market(s)

People dealing in commercial property

Industry/Entity Type

Business

Contact Information for Business Card

KT Estates Australia
Peter Moss Mobile0419 703 646
Email Peter@birchvale-sample.com.au

Font styles to use
Sans Serif

Requirements
Must have
• company name
• contact details
Nice to have
• KT Estates Bold
• Australia Not Bold
Should not have
• To busy of a look

```html
<!DOCTYPE html>
<html lang="en">
<head>
<meta charset="utf-8">
<title>KT Estates Australia – Business Card</title>
<link href="https://fonts.googleapis.com/css2?family=Ubuntu:wght@400;500;700&display=swap" rel="stylesheet">
<style>
  :root {
    --page-bg: #eef0f3;
    --card-white: #ffffff;
    --card-mist: #e9eaee;
    --brand-navy: #25308c;
    --brand-red: #d61f33;
    --band-red: #d42236;
    --band-magenta: #9b2a6a;
    --band-purple: #553392;
    --text-light: #ffffff;
    --rule-light: rgba(255, 255, 255, 0.7);
  }
  * { margin: 0; padding: 0; box-sizing: border-box; }
  html, body {
    width: 1200px;
    height: 800px;
    overflow: hidden;
    background: var(--page-bg);
    font-family: "Ubuntu", sans-serif;
  }
  .canvas {
    width: 1200px;
    height: 800px;
    display: flex;
    align-items: center;
    justify-content: center;
  }
  .business-card {
    position: relative;
    width: 900px;
    height: 520px;
    background: linear-gradient(180deg, var(--card-white) 0%, var(--card-white) 30%, var(--card-mist) 58%);
    box-shadow: 0 12px 36px rgba(20, 20, 40, 0.18);
    overflow: hidden;
  }
  .brand-lockup {
    position: absolute;
    top: 92px;
    left: 0;
    right: 0;
    display: flex;
    align-items: center;
    justify-content: center;
    gap: 16px;
  }
  .brand-mark {
    width: 26px;
    height: 26px;
    background: var(--brand-red);
  }
  .brand-name {
    font-weight: 700;
    font-size: 44px;
    letter-spacing: 0.5px;
    color: var(--brand-navy);
  }
  .skyline-band {
    position: absolute;
    left: 0;
    right: 0;
    top: 245px;
    bottom: 0;
    background: linear-gradient(90deg, var(--band-red) 0%, var(--band-magenta) 50%, var(--band-purple) 100%);
  }
  .card-holder {
    position: absolute;
    left: 0;
    right: 0;
    top: 365px;
    text-align: center;
    color: var(--text-light);
  }
  .holder-name {
    font-weight: 500;
    font-size: 40px;
    letter-spacing: 1.5px;
    text-transform: uppercase;
  }
  .holder-rule {
    width: 660px;
    height: 1px;
    margin: 14px auto 12px;
    background: var(--rule-light);
  }
  .holder-contact {
    font-weight: 400;
    font-size: 24px;
  }
  .holder-contact .divider { margin: 0 6px; }
</style>
</head>
<body>
  <main class="canvas">
    <article class="business-card">
      <div class="brand-lockup">
        <span class="brand-mark"></span>
        <span class="brand-name">KT Estates Australia</span>
      </div>
      <div class="skyline-band" role="img" aria-label="City skyline silhouette with harbour bridge and opera house in a red to purple gradient"></div>
      <div class="card-holder">
        <h1 class="holder-name">Peter Moss</h1>
        <div class="holder-rule"></div>
        <p class="holder-contact">M: 0455 218 907<span class="divider">|</span>E: Peter@birchvale-sample.com.au</p>
      </div>
    </article>
  </main>
</body>
</html>
```